Creat new BusinessCard for Brightpath Advisory!

Hello Creativ Designer. I need a new Businesscard for our brand new Company "Brightpath Coaching". We do Consulting for a better Life & Work Situation. to create Fulfillment, Sense, Motivation and healthy Work Places in Company's. So we try to create a better World and help the employee to like what they do!
So we would like to have 2 Sites on the card. On the Back we want to put this words: "The sole meaning of life, is to serve humanity" (it can be vertical oder horizontal). In the front there is the Logo (Black or White) and Adress+ and Slogan.

Slogan on the front: -Make your Business & Life to a better place-

Name: Lukas Fenwald
Titel: Founder - Visionary - Trainer
Adress: Based in Switzerland

Tel: +41 (0) 71 483 27 15
Email: hello@brightpath-coaching.ch
Homepage: www.brightpath-coaching.ch

Thanks for your inspired Ideas and your help to make the world to a better place! IT has to be ready to print and normal Size.

Target Market(s)

insurance, Bank, Telecom, industry, IT, Medical

Contact Information for Business Card

Breite: 85 mm x Höhe: 55 mm

Colors

Designer to choose colors to be used in the design.

Requirements
Nice to have
• Thanks for your Ideas so far!
• Maybe you can try/play with the colors: Purple Code #652C8F and Grey #979797 from the Zorvik Logo purple and grey (but only a soft combination, not to much)

```html
<!DOCTYPE html>
<html lang="en">
<head>
<meta charset="utf-8">
<title>Brightpath Coaching – Business Card</title>
<link href="https://fonts.googleapis.com/css2?family=Lato:wght@400;700;900&display=swap" rel="stylesheet">
<style>
  :root {
    --page-bg: #d9dadf;
    --front-bg: #1d1d1f;
    --back-bg: #2b2e3b;
    --purple: #8048b8;
    --purple-soft: #9a6cc9;
    --grey-text: #b9b9bd;
    --light-text: #e4e4e8;
    --map-tone: rgba(255,255,255,0.045);
    --white-mark: #f2f2f2;
  }
  * { box-sizing: border-box; margin: 0; padding: 0; }
  html, body { width: 1200px; height: 900px; overflow: hidden; }
  body {
    background: var(--page-bg);
    font-family: "Lato", Arial, sans-serif;
    position: relative;
  }
  .card {
    position: absolute;
    width: 560px;
    height: 362px;
    border-radius: 6px;
    overflow: hidden;
    box-shadow: 0 14px 30px rgba(0,0,0,0.28);
  }
  .card--front { left: 100px; top: 60px; background: var(--front-bg); }
  .card--back { left: 540px; top: 478px; background: var(--back-bg); }

  .world-map {
    position: absolute;
    left: 60px; top: 40px; width: 440px; height: 260px;
    border-radius: 40% 45% 38% 50%;
    background: radial-gradient(ellipse at center, var(--map-tone), transparent 72%);
  }

  .brand {
    position: absolute;
    display: flex;
    align-items: center;
    gap: 12px;
  }
  .brand__dot {
    width: 54px; height: 54px; border-radius: 50%;
    background: linear-gradient(180deg, #9b63d1, #6a35a0);
    flex: none;
  }
  .brand__name {
    font-weight: 700;
    font-size: 24px;
    letter-spacing: 1px;
    text-transform: uppercase;
    color: var(--grey-text);
    line-height: 1.1;
  }
  .card--front .brand { left: 34px; top: 70px; }
  .card--back .brand { left: 50%; top: 120px; transform: translateX(-50%); }
  .card--back .brand__dot { width: 64px; height: 64px; }
  .card--back .brand__name { font-size: 28px; }

  .slogan {
    position: absolute;
    left: 34px; bottom: 40px;
    font-size: 14px;
    color: var(--grey-text);
  }

  .divider {
    position: absolute;
    left: 280px; top: 60px;
    width: 2px; height: 150px;
    background: linear-gradient(180deg, var(--purple), transparent);
    transform: rotate(28deg);
    transform-origin: top;
  }

  .contact-block {
    position: absolute;
    left: 300px; top: 150px;
  }
  .person__name {
    font-weight: 900;
    font-size: 24px;
    color: var(--purple);
    text-transform: uppercase;
    letter-spacing: 0.5px;
  }
  .person__title {
    font-size: 13px;
    color: var(--grey-text);
    margin: 4px 0 18px;
  }
  .contact-list { list-style: none; }
  .contact-item {
    display: flex; align-items: center; gap: 10px;
    font-size: 13px; color: var(--light-text);
    margin-bottom: 10px;
  }
  .contact-icon {
    width: 22px; height: 22px; border-radius: 50%;
    background: var(--purple);
    display: flex; align-items: center; justify-content: center;
    flex: none;
  }

  .motto {
    position: absolute;
    left: 0; right: 0; top: 240px;
    display: flex; align-items: center; justify-content: center; gap: 12px;
    font-size: 14px;
    letter-spacing: 0.6px;
    color: var(--light-text);
    text-transform: uppercase;
  }
  .motto__mark { width: 9px; height: 14px; background: var(--white-mark); }
</style>
</head>
<body>

<section class="card card--front" aria-label="Business card front">
  <div class="world-map" role="img" aria-label="Faint dotted world map in the background"></div>
  <div class="brand">
    <span class="brand__dot"></span>
    <span class="brand__name">Brightpath<br>Coaching</span>
  </div>
  <p class="slogan">Make Your Business &amp; Life to a better Place</p>
  <div class="divider"></div>
  <div class="contact-block">
    <h1 class="person__name">Lukas Fenwald</h1>
    <p class="person__title">Founder - Visionary - Trainer</p>
    <ul class="contact-list">
      <li class="contact-item">
        <span class="contact-icon">
          <svg width="12" height="12" viewBox="0 0 24 24" fill="none" stroke="#fff" stroke-width="2"><path d="M5 3h4l2 5-2.5 1.5a11 11 0 0 0 6 6L16 13l5 2v4a2 2 0 0 1-2 2A16 16 0 0 1 3 5a2 2 0 0 1 2-2z"/></svg>
        </span>
        +41 (0) 71 483 27 15
      </li>
      <li class="contact-item">
        <span class="contact-icon">
          <svg width="12" height="12" viewBox="0 0 24 24" fill="none" stroke="#fff" stroke-width="2"><rect x="3" y="5" width="18" height="14" rx="1"/><path d="M3 6l9 7 9-7"/></svg>
        </span>
        hello@brightpath-coaching.ch
      </li>
      <li class="contact-item">
        <span class="contact-icon">
          <svg width="12" height="12" viewBox="0 0 24 24" fill="none" stroke="#fff" stroke-width="2"><rect x="7" y="3" width="10" height="18" rx="5"/><path d="M12 7v4"/></svg>
        </span>
        www.brightpath-coaching.ch
      </li>
    </ul>
  </div>
</section>

<section class="card card--back" aria-label="Business card back">
  <div class="world-map" role="img" aria-label="Faint dotted world map in the background"></div>
  <div class="brand">
    <span class="brand__dot"></span>
    <span class="brand__name">Brightpath<br>Coaching</span>
  </div>
  <p class="motto">
    <span class="motto__mark"></span>
    The sole meaning of life, is to serve humanity
    <span class="motto__mark"></span>
  </p>
</section>

</body>
</html>
```